Harbor fairly.com a website to help those harmed by lending institutions

I am looking for a basic one page website that will be used to collect data from people filling out a form.
I will need certain key words to be optimized in order for the page to show up as high as possible in the search engines.

This web page is for people that have been harmed by their. Bank or lending institution due to inappropriate accounting practices or worse purposeful neglect.

Imagery should include an elderly person on the phone in distress because of over due bills.

Images of late notices
Images of threats of foreclosure.

** This site is to help people that are being unfairly treated even though they have made all their payments on time and the bank is commiting gross negligence.***

Some basic notes to start:

The color scheme should be similar to this site:

https://www.plovermark.example/

Here are some basic notes.

There will be more to follow.

There will need to be a collection form that people can link to and share their story.

Have you or someone you loved been hurt by their financial lending institution?

Have they/ you made all your payments on time only to constantly receive late notice penalties and additional accrued interest ?
Has your credit and good name been tarnished because your banks negligent or purposeful mis-handling of your account has caused the credit bureaus to drop your credit score?
Do you spend hours each month calling your bank to have them clear up their accounting mistakes?
Have you received threatening foreclosure notices even though you've made every payment on time ?

Well if so, you are not alone! This practise or gross incompetence is happening to many others just like you.

Your mortgage, student loan out other debt may have been sold to a new company that simply keeps losing the payments and you have to constantly clear you their errors on your time over and over again.

Budget is flexible based on design.

```html
<!DOCTYPE html>
<html lang="en">
<head>
<meta charset="utf-8">
<title>Harbor fairly.com – Help for people harmed by lending institutions</title>
<link rel="stylesheet" href="https://fonts.googleapis.com/css2?family=Jost:wght@400;500;600;700&family=Lato:ital,wght@0,400;0,700;0,900;1,700&display=swap">
<style>
:root{
  --green:#15895f;
  --green-dark:#0f7650;
  --orange:#ef7d1f;
  --ink:#222222;
  --text:#555555;
  --muted:#7a7a7a;
  --hero-bg:#e4e4e4;
  --ring:#d0d0d0;
  --soft:#f3f3f3;
  --footer:#323232;
  --footer-deep:#262626;
  --line:#cfcfcf;
  --white:#ffffff;
}
*{box-sizing:border-box;margin:0;padding:0}
html,body{width:1200px;height:3285px;overflow:hidden}
body{position:relative;font-family:'Lato',Arial,sans-serif;color:var(--text);background:var(--white)}
.abs{position:absolute}
.heading-font{font-family:'Jost',Arial,sans-serif}

/* header */
.site-header{position:absolute;left:0;top:0;width:1200px;height:103px;background:var(--white)}
.brand{position:absolute;left:145px;top:30px;display:flex;align-items:center;gap:12px;font-family:'Jost',Arial,sans-serif;font-weight:600;font-size:30px;letter-spacing:1px;color:var(--green)}
.brand-dot{width:20px;height:20px;border-radius:50%;background:var(--orange)}
.call-us{position:absolute;right:145px;top:18px;font-family:'Lato',Arial,sans-serif;font-size:19px;font-weight:700;color:var(--ink);display:flex;align-items:center;gap:10px}
.main-nav{position:absolute;left:561px;top:63px;display:flex;font-size:15px;font-weight:700;color:var(--ink)}
.main-nav span{margin-right:40px}
.search-icon{position:absolute;left:1038px;top:64px}

/* hero */
.hero{position:absolute;left:0;top:103px;width:1200px;height:593px;background:var(--hero-bg);overflow:hidden}
.hero-title{position:absolute;left:145px;top:218px;font-family:'Jost',Arial,sans-serif;font-weight:600;font-size:58px;letter-spacing:3px;color:var(--ink);line-height:1}
.hero-lead{position:absolute;left:145px;top:305px;width:430px;font-size:20px;line-height:34px;color:var(--text)}
.btn-pill{display:inline-flex;align-items:center;justify-content:center;gap:8px;background:var(--orange);color:var(--white);font-weight:900;font-size:14px;border-radius:30px;text-transform:uppercase;letter-spacing:.5px}
.hero-btn{position:absolute;left:145px;top:400px;width:155px;height:44px}
.slider-dots{position:absolute;left:145px;top:520px;display:flex;gap:9px}
.slider-dots i{width:9px;height:9px;border-radius:50%;background:#b9b9b9}
.slider-dots i.on{background:var(--green)}

/* contact form */
.say-hello{position:absolute;left:0;top:696px;width:1200px;height:353px;background:var(--green);box-shadow:0 18px 24px -12px rgba(0,0,0,.45);z-index:2}
.say-hello h2{position:absolute;left:0;top:40px;width:1200px;text-align:center;font-family:'Jost',Arial,sans-serif;font-weight:600;font-size:42px;letter-spacing:2px;color:var(--white)}
.form-row{position:absolute;left:145px;width:910px;display:flex;gap:12px}
.form-row.first{top:123px}
.form-row.second{top:178px}
.field{flex:1;height:40px;background:var(--white);border:1px solid #d8d8d8;font-size:14px;color:var(--text);padding:0 14px;display:flex;align-items:center;justify-content:space-between}
.submit-btn{position:absolute;left:508px;top:246px;width:184px;height:57px;font-size:20px;letter-spacing:1px}

/* about */
.about{position:absolute;left:0;top:1049px;width:1200px;height:583px;background:linear-gradient(90deg,#f7f7f7,#fcfcfc 45%,#f4f4f4)}
.about-frame{position:absolute;left:145px;top:112px;width:376px;height:374px;border:1.5px solid #5a5a5a}
.about-vertical{position:absolute;left:150px;top:248px;transform:rotate(-90deg);transform-origin:left top;font-family:'Jost',Arial,sans-serif;font-weight:700;font-size:24px;letter-spacing:2px;color:var(--green);white-space:nowrap;top:410px;left:160px}
.about-photo{position:absolute;left:212px;top:162px;width:390px;height:278px;background:linear-gradient(135deg,#eef0f2,#d9dde2 55%,#c9a79b)}
.ghost-word{position:absolute;font-family:'Jost',Arial,sans-serif;font-weight:600;color:rgba(0,0,0,.06);letter-spacing:4px;line-height:1;white-space:nowrap}
.section-title{position:absolute;font-family:'Jost',Arial,sans-serif;font-weight:600;font-size:34px;letter-spacing:1.5px;color:var(--ink);line-height:1}
.title-rule{position:absolute;height:2px;width:70px;background:var(--orange)}
.about-text{position:absolute;left:670px;top:205px;width:390px;font-size:14.5px;line-height:30.5px;color:var(--muted)}
.about-btn{position:absolute;left:670px;top:423px;width:147px;height:43px}

/* services */
.services{position:absolute;left:0;top:1632px;width:1200px;height:617px;background:var(--soft)}
.card-grid{position:absolute;left:140px;top:225px;display:flex;gap:19px}
.service-card{position:relative;width:218px;height:280px;background:var(--white);box-shadow:0 2px 8px rgba(0,0,0,.18);padding:5px;overflow:hidden}
.card-photo{width:208px;height:155px}
.card-icon{position:absolute;left:85px;top:136px;width:48px;height:48px;border-radius:50%;background:var(--orange);border:3px solid var(--white);display:flex;align-items:center;justify-content:center}
.card-title{margin:42px 0 0 14px;font-family:'Lato',Arial,sans-serif;font-weight:900;font-size:13px;color:var(--ink);text-transform:uppercase}
.card-text{margin:9px 14px 0 14px;font-size:12px;line-height:20px;color:var(--muted)}
.card-corner{position:absolute;right:0;bottom:0;width:44px;height:44px}

/* faq */
.faq{position:absolute;left:0;top:2249px;width:1200px;height:664px;background:linear-gradient(90deg,#f8f8f8,#fdfdfd 50%,#f5f5f5)}
.faq-art{position:absolute;left:0;top:254px;width:372px;height:262px;border-radius:0 140px 140px 0;background:linear-gradient(90deg,#9cc23d,#d82a7e 45%,#4fb4dd)}
.faq-list{position:absolute;left:423px;top:206px;width:630px;display:flex;flex-direction:column;gap:14px}
.faq-item{background:var(--white);border:1px solid var(--line)}
.faq-q{position:relative;padding:8px 56px 8px 15px;font-family:'Lato',Arial,sans-serif;font-style:italic;font-weight:700;font-size:12.5px;line-height:19px;color:var(--ink);min-height:42px;display:flex;align-items:center}
.faq-item.open .faq-q{background:var(--orange);color:var(--white)}
.faq-a{padding:9px 15px 10px;font-size:12.5px;line-height:19px;color:var(--text)}
.toggle{position:absolute;right:10px;top:50%;margin-top:-12px;width:24px;height:24px;border-radius:50%;background:var(--green);color:var(--white);font-family:'Lato',Arial,sans-serif;font-style:normal;font-weight:900;font-size:18px;line-height:24px;text-align:center}
.faq-item.open .toggle{background:var(--white);color:var(--orange)}

/* footer */
.site-footer{position:absolute;left:0;top:2913px;width:1200px;height:317px;background:var(--footer);color:#e6e6e6}
.footer-col{position:absolute;top:88px}
.footer-col h3{font-family:'Lato',Arial,sans-serif;font-weight:900;font-size:15px;color:var(--white);text-transform:uppercase;letter-spacing:.5px;margin-bottom:22px}
.quick-links li{list-style:none;font-size:12px;line-height:26px;display:flex;align-items:center;gap:14px}
.quick-links li::before{content:"»";font-size:13px;color:var(--white)}
.contact-line{display:flex;gap:16px;font-size:12px;line-height:18px;margin-bottom:16px}
.contact-line svg{flex:none;margin-top:2px}
.news-text{font-size:12px;line-height:18px;width:220px}
.news-input{margin-top:15px;width:211px;height:34px;border:1px solid #8a8a8a;font-size:11px;padding:0 12px;display:flex;align-items:center}
.news-btn{margin-top:16px;width:96px;height:31px;background:var(--green);color:var(--white);font-size:11px;font-weight:900;text-transform:uppercase;display:flex;align-items:center;justify-content:center}
.social-grid{display:grid;grid-template-columns:repeat(3,36px);gap:12px 10px}
.social-grid i{width:36px;height:34px;border:1.5px solid #bdbdbd;display:block}
.bottom-bar{position:absolute;left:0;top:3230px;width:1200px;height:55px;background:var(--footer-deep)}
.bottom-bar svg{position:absolute;left:0;top:0}
.copyright{position:absolute;left:145px;top:20px;font-size:11px;color:var(--white)}
</style>
</head>
<body>

<header class="site-header">
  <div class="brand"><span class="brand-dot"></span>HARBOR FAIRLY</div>
  <div class="call-us">
    <svg width="18" height="18" viewBox="0 0 24 24" aria-hidden="true"><path fill="#ef7d1f" d="M6.6 10.8a15.1 15.1 0 0 0 6.6 6.6l2.2-2.2a1 1 0 0 1 1-.25 11.4 11.4 0 0 0 3.6.57 1 1 0 0 1 1 1V20a1 1 0 0 1-1 1A17 17 0 0 1 3 4a1 1 0 0 1 1-1h3.5a1 1 0 0 1 1 1c0 1.25.2 2.45.57 3.57a1 1 0 0 1-.25 1z"/></svg>
    Call Us : 1 888 888 8888
  </div>
  <nav class="main-nav"><span>Home</span><span>What We Do</span><span>Who We Are</span><span>News</span><span>Contact us</span></nav>
  <svg class="search-icon" width="17" height="17" viewBox="0 0 24 24" aria-hidden="true"><circle cx="10" cy="10" r="7" fill="none" stroke="#15895f" stroke-width="3"/><path d="M15 15l6 6" stroke="#15895f" stroke-width="3" stroke-linecap="round"/></svg>
</header>

<section class="hero">
  <svg class="abs" style="left:0;top:0" width="1200" height="593" aria-hidden="true">
    <rect x="460" y="92" width="58" height="46" rx="23" fill="#d3d3d3"/>
    <rect x="498" y="92" width="170" height="26" rx="13" fill="#d3d3d3"/>
    <rect x="540" y="126" width="130" height="22" rx="11" fill="#d3d3d3"/>
    <circle cx="960" cy="345" r="318" fill="none" stroke="var(--ring)" stroke-width="34"/>
  </svg>
  <svg class="abs" style="left:640px;top:0" width="560" height="593" role="img" aria-label="Photo of a worried man on the phone at his laptop">
    <defs><linearGradient id="heroPhoto" x1="0" y1="0" x2="1" y2="1"><stop offset="0" stop-color="#f1f1f1"/><stop offset=".5" stop-color="#9fb4d1"/><stop offset="1" stop-color="#6f86aa"/></linearGradient></defs>
    <circle cx="320" cy="345" r="300" fill="url(#heroPhoto)"/>
  </svg>
  <h1 class="hero-title">HARBOR FAIRLY</h1>
  <p class="hero-lead">Have you or someone you loved been hurt by their financial lending institution?</p>
  <div class="btn-pill hero-btn">Read More
    <svg width="14" height="14" viewBox="0 0 16 16" aria-hidden="true"><circle cx="8" cy="8" r="7" fill="#fff"/><path d="M6.5 4.5L10 8l-3.5 3.5" stroke="#ef7d1f" stroke-width="2" fill="none"/></svg>
  </div>
  <div class="slider-dots"><i></i><i></i><i></i><i class="on"></i><i></i><i></i></div>
</section>

<section class="say-hello">
  <h2>SAY HELLO</h2>
  <div class="form-row first">
    <div class="field">Enter Name</div>
    <div class="field">Email Address</div>
    <div class="field">Phone Number</div>
    <div class="field">Address</div>
  </div>
  <div class="form-row second">
    <div class="field">Name of the institution</div>
    <div class="field">Types Of Issue
      <svg width="10" height="6" viewBox="0 0 10 6" aria-hidden="true"><path d="M0 0h10L5 6z" fill="#555"/></svg>
    </div>
    <div class="field">How we Can Help?</div>
  </div>
  <div class="btn-pill submit-btn">Submit</div>
</section>

<section class="about">
  <div class="about-frame"></div>
  <div class="about-vertical">HARBOR FAIRLY</div>
  <div class="about-photo" role="img" aria-label="Photo of hands pointing at financial papers and charts on a desk"></div>
  <div class="ghost-word" style="left:672px;top:92px;font-size:80px">ABOUT US</div>
  <h2 class="section-title" style="left:670px;top:130px">ABOUT US</h2>
  <div class="title-rule" style="left:670px;top:176px"></div>
  <p class="about-text">Lorem ipsum dolor sit amet, consectetur adipiscing elit, sed do eiusmod tempor incididunt ut labore et dolore magna aliqua. Ut enim ad minim veniam, quis nostrud exercitation ullamco laboris nisi ut aliquip ex ea commodo consequat. aute irure dolor in reprehenderit in voluptate velit esse cillum dolore eu fugiat nulla pariatxcepteur</p>
  <div class="btn-pill about-btn">Read More</div>
</section>

<section class="services">
  <div class="ghost-word" style="left:0;width:1200px;text-align:center;top:88px;font-size:80px">SERVICES</div>
  <h2 class="section-title" style="left:0;width:1200px;text-align:center;top:108px">WHAT WE DO</h2>
  <div class="title-rule" style="left:565px;top:154px"></div>
  <div class="card-grid">
    <article class="service-card">
      <div class="card-photo" role="img" aria-label="Photo of a hand signing an overdue notice" style="background:linear-gradient(135deg,#e9ecf1,#b9c3d3 60%,#c88484)"></div>
      <div class="card-icon"><svg width="20" height="20" viewBox="0 0 24 24" aria-hidden="true"><rect x="4" y="4" width="14" height="16" rx="2" fill="none" stroke="#fff" stroke-width="2"/><path d="M9 15l9-9" stroke="#fff" stroke-width="2"/></svg></div>
      <h3 class="card-title">Lorem Ips Dolor</h3>
      <p class="card-text">Lorem ipsum dolor sit amet, con-sectetur adipiscing elit,</p>
      <svg class="card-corner" viewBox="0 0 44 44" aria-hidden="true"><path d="M44 0V44H0z" fill="var(--green)"/><path d="M31 26v12M25 32h12" stroke="#fff" stroke-width="2.5"/></svg>
    </article>
    <article class="service-card">
      <div class="card-photo" role="img" aria-label="Photo of a woman in a consultation meeting" style="background:linear-gradient(135deg,#8a6a55,#c89a7d 50%,#e3d6c8)"></div>
      <div class="card-icon"><svg width="20" height="20" viewBox="0 0 24 24" aria-hidden="true"><circle cx="12" cy="8" r="4" fill="none" stroke="#fff" stroke-width="2"/><path d="M4 21c1-5 15-5 16 0" fill="none" stroke="#fff" stroke-width="2"/></svg></div>
      <h3 class="card-title">Architecto Beat</h3>
      <p class="card-text">Lorem ipsum dolor sit amet, con-sectetur adipiscing elit,</p>
      <svg class="card-corner" viewBox="0 0 44 44" aria-hidden="true"><path d="M44 0V44H0z" fill="var(--green)"/><path d="M31 26v12M25 32h12" stroke="#fff" stroke-width="2.5"/></svg>
    </article>
    <article class="service-card">
      <div class="card-photo" role="img" aria-label="Photo of a stressed man holding his head" style="background:linear-gradient(135deg,#3f4a56,#6c7a88 55%,#a9b3bc)"></div>
      <div class="card-icon"><svg width="20" height="20" viewBox="0 0 24 24" aria-hidden="true"><path d="M5 19l2-6 9-9 4 4-9 9z" fill="none" stroke="#fff" stroke-width="2"/></svg></div>
      <h3 class="card-title">Lorem Ips Dolor</h3>
      <p class="card-text">Lorem ipsum dolor sit amet, con-sectetur adipiscing elit,</p>
      <svg class="card-corner" viewBox="0 0 44 44" aria-hidden="true"><path d="M44 0V44H0z" fill="var(--green)"/><path d="M31 26v12M25 32h12" stroke="#fff" stroke-width="2.5"/></svg>
    </article>
    <article class="service-card">
      <div class="card-photo" role="img" aria-label="Photo of hands holding a final notice envelope" style="background:linear-gradient(135deg,#f2f2f2,#d6d6d6 55%,#c97b7b)"></div>
      <div class="card-icon"><svg width="20" height="20" viewBox="0 0 24 24" aria-hidden="true"><path d="M3 7h7l2 2h9v10H3z" fill="none" stroke="#fff" stroke-width="2"/></svg></div>
      <h3 class="card-title">Architecto Beat</h3>
      <p class="card-text">Lorem ipsum dolor sit amet, con-sectetur adipiscing elit,</p>
      <svg class="card-corner" viewBox="0 0 44 44" aria-hidden="true"><path d="M44 0V44H0z" fill="var(--green)"/><path d="M31 26v12M25 32h12" stroke="#fff" stroke-width="2.5"/></svg>
    </article>
  </div>
</section>

<section class="faq">
  <div class="ghost-word" style="left:420px;top:80px;font-size:82px">QUESTIONS</div>
  <h2 class="section-title" style="left:420px;top:116px">FAQ</h2>
  <div class="title-rule" style="left:420px;top:160px"></div>
  <div class="faq-art" role="img" aria-label="Illustration of colourful speech bubbles spelling FAQ"></div>
  <div class="faq-list">
    <div class="faq-item open">
      <div class="faq-q">Have they/ you made all your payments on time only to constantly receive late notice penalties and additional accrued interest ?<span class="toggle">−</span></div>
      <div class="faq-a">There are many variations of passages of Lorem Ipsum available, but the majority have suffered alteration in some form, by injected humour.</div>
    </div>
    <div class="faq-item"><div class="faq-q">Has your credit and good name been tarnished because your banks negligent or purposeful mis-handling of your account has caused the credit bureaus to drop your credit score?<span class="toggle">+</span></div></div>
    <div class="faq-item"><div class="faq-q">Do you spend hours each month calling your bank to have them clear up their accounting mistakes?<span class="toggle">+</span></div></div>
    <div class="faq-item"><div class="faq-q">Have you received threatening foreclosure notices even though you've made every payment on time ?<span class="toggle">+</span></div></div>
    <div class="faq-item"><div class="faq-q" style="min-height:62px">Have you received threatening foreclosure notices even though you've made every payment on time ?<span class="toggle">+</span></div></div>
  </div>
</section>

<footer class="site-footer">
  <div class="footer-col" style="left:145px">
    <h3>Quick Links</h3>
    <ul class="quick-links"><li>Home</li><li>What We Do</li><li>Who We Are</li><li>News</li><li>Contact us</li></ul>
  </div>
  <div class="footer-col" style="left:346px;width:230px">
    <h3>Contact Us</h3>
    <div class="contact-line"><svg width="14" height="18" viewBox="0 0 14 18" aria-hidden="true"><path d="M7 1a6 6 0 0 1 6 6c0 4.5-6 10-6 10S1 11.5 1 7a6 6 0 0 1 6-6z" fill="none" stroke="#ddd" stroke-width="1.4"/><circle cx="7" cy="7" r="2" fill="none" stroke="#ddd" stroke-width="1.4"/></svg><span>123,Sed ut perspiciatis unde omni iste natus error sivoluptatem</span></div>
    <div class="contact-line"><svg width="16" height="16" viewBox="0 0 24 24" aria-hidden="true"><path fill="none" stroke="#ddd" stroke-width="1.8" d="M6.6 10.8a15.1 15.1 0 0 0 6.6 6.6l2.2-2.2a1 1 0 0 1 1-.25 11.4 11.4 0 0 0 3.6.57 1 1 0 0 1 1 1V20a1 1 0 0 1-1 1A17 17 0 0 1 3 4a1 1 0 0 1 1-1h3.5a1 1 0 0 1 1 1c0 1.25.2 2.45.57 3.57a1 1 0 0 1-.25 1z"/></svg><span>Phone: 1 888 888 8888</span></div>
    <div class="contact-line"><svg width="16" height="14" viewBox="0 0 16 14" aria-hidden="true"><rect x="1" y="2" width="14" height="10" fill="none" stroke="#ddd" stroke-width="1.4"/><path d="M1 2l7 6 7-6" fill="none" stroke="#ddd" stroke-width="1.4"/></svg><span>info@companyname.com</span></div>
  </div>
  <div class="footer-col" style="left:637px">
    <h3>Sign Up Newsletter</h3>
    <p class="news-text">Sed ut perspiciatis unde omnis iste natu</p>
    <div class="news-input">Email Address</div>
    <div class="news-btn">Sign Up</div>
  </div>
  <div class="footer-col" style="left:869px">
    <h3>Social Media</h3>
    <div class="social-grid"><i></i><i></i><i></i><i></i><i></i><i></i></div>
  </div>
</footer>

<div class="bottom-bar">
  <svg width="520" height="55" aria-hidden="true"><path d="M0 0H470L515 55H0z" fill="var(--orange)"/></svg>
  <span class="copyright">Copyright 2019 © Companyname.All Rights Reserved</span>
</div>

</body>
</html>
```